RESIDENCE VALBRUNETTE

The CORVALIS Immobilier company exclusively offers apartments for sale under a tax exemption law (BRESSAUTINIÉ) in CAMBRAI, 92 apartments are available, fully renovated with balcony, terrace, elevator, in a former military residence known to the city.
We want to make a book to give to our customers.

```html
<!DOCTYPE html>
<html lang="fr">
<head>
<meta charset="utf-8">
<title>Guide Bressautinié – Résidence Valbrunette</title>
<link rel="stylesheet" href="https://fonts.googleapis.com/css2?family=Open+Sans:wght@300;400;600&display=swap">
<style>
  :root {
    --backdrop: #e6e6e6;
    --paper: #f7f7f7;
    --paper-fold: #e4e4e4;
    --frame-green: #5dbf93;
    --accent-green: #4fb386;
    --ink: #222628;
    --ink-soft: #4a4f52;
    --ink-light: #6c7174;
    --navy: #2f3d6b;
    --link-blue: #3a54a6;
  }
  * { box-sizing: border-box; margin: 0; padding: 0; }
  html, body {
    width: 1200px; height: 800px; overflow: hidden;
    background: var(--backdrop);
    font-family: "Open Sans", "Segoe UI", sans-serif;
    color: var(--ink);
  }
  .spread {
    position: absolute; left: 40px; top: 205px;
    width: 1120px; height: 390px;
    display: flex;
    box-shadow: 0 10px 30px rgba(0,0,0,.12);
  }
  .page {
    position: relative; width: 560px; height: 390px;
    background: var(--paper);
  }
  .page--left { background: linear-gradient(to right, var(--paper) 88%, var(--paper-fold)); }
  .page--right { background: linear-gradient(to left, var(--paper) 88%, var(--paper-fold)); }
  .page__frame {
    position: absolute; inset: 24px;
    border: 2px solid var(--frame-green);
  }
  .guide-badge {
    position: absolute; top: 34px; right: 36px; width: 48px;
    text-align: center;
  }
  .guide-badge__cover {
    width: 48px; height: 62px;
    background: linear-gradient(160deg, #7fd3ac, var(--frame-green) 70%, #2b2f31 100%);
  }
  .guide-badge__link {
    display: block; margin-top: 2px;
    font-size: 4.5px; color: var(--link-blue); text-decoration: underline;
    white-space: nowrap;
  }
  .section { position: absolute; }
  .section__title {
    font-weight: 600; font-size: 19px; color: var(--ink); margin-bottom: 18px;
  }
  .section__text {
    font-size: 8.6px; line-height: 1.45; color: var(--ink-soft); margin-bottom: 10px;
  }
  .highlight { color: var(--accent-green); }
  .page--left .section { left: 130px; top: 150px; width: 340px; }
  .page--right .section { left: 100px; top: 95px; width: 360px; }
  .works__lead {
    font-weight: 300; font-size: 14px; color: var(--ink-light);
    margin: 42px 0 28px 40px;
  }
  .works__item { display: flex; align-items: flex-start; gap: 18px; margin-left: 55px; }
  .works__icon { flex: 0 0 34px; margin-top: 12px; }
  .works__text { font-size: 8.6px; line-height: 1.35; color: var(--ink-soft); }
</style>
</head>
<body>
  <main class="spread">
    <section class="page page--left">
      <div class="page__frame"></div>
      <div class="guide-badge">
        <div class="guide-badge__cover" role="img" aria-label="Vignette de couverture du guide Bressautinié"></div>
        <span class="guide-badge__link">guide-bressautinie.fr</span>
      </div>
      <div class="section">
        <h2 class="section__title">Qui peut en bénéficier ?</h2>
        <p class="section__text">Réaliser un investissement en Loi Bressautinié quel que soit votre <span class="highlight">niveau d’imposition</span>.</p>
        <p class="section__text">Le dispositif Bressautinié est réservé aux contribuables français qui réalisent des <span class="highlight">investissements locatifs</span> directement ou via des sociétés non soumises à l’impôt sur les sociétés (SCI ou SCPI) entre le 1er janvier 2015 et le 31 décembre 2021.</p>
      </div>
    </section>

    <section class="page page--right">
      <div class="page__frame"></div>
      <div class="guide-badge">
        <div class="guide-badge__cover" role="img" aria-label="Vignette de couverture du guide Bressautinié"></div>
        <span class="guide-badge__link">guide-bressautinie.fr</span>
      </div>
      <div class="section">
        <h2 class="section__title">Les logements éligibles</h2>
        <p class="section__text">Les conditions d’éligibilité d’un logement en loi Bressautinié :</p>
        <p class="section__text">Pour pouvoir prétendre à la réduction d’impôt de la Loi Bressautinié, il est nécessaire d’investir dans un logement situé dans <span class="highlight">l’une des 222 communes</span> bénéficiaires du plan <span class="highlight">Centres Vivants</span>, mis en place par le gouvernement.</p>
        <p class="works__lead">Les travaux de rénovations devront :</p>
        <div class="works__item">
          <svg class="works__icon" width="34" height="34" viewBox="0 0 34 34" aria-hidden="true">
            <circle cx="17" cy="17" r="15" fill="none" stroke="var(--navy)" stroke-width="2"/>
            <polyline points="14,11 20,17 14,23" fill="none" stroke="var(--navy)" stroke-width="2.5" stroke-linecap="round" stroke-linejoin="round"/>
          </svg>
          <p class="works__text">Améliorer la performance énergétique du logement<br>d’au moins 30% (20% en habitat collectif) ,<br>Ou bien représenter 2 types de travaux sur un choix<br>de 5. Lesquels sont :</p>
        </div>
      </div>
    </section>
  </main>
</body>
</html>
```